Founder / concept developer needs business card // Consultant needs VCARD

I need a business card for me as a founding consultant in Berlin. I advise entrepreneurs, especially in the design of business ideas, business plans or financing applications. More information about this in the annexes. My USP: I design / structure complex ideas and projects convincingly so that my client is successful. I want to communicate professionalism, effectiveness and clarity. Colors like from the range BLACK-GRAY-GREEN. I am 27 years old, I have studied business for 7 years. Attachments: - Business card design (only idea, do not focus on it) - Website screenshot (only idea, do not focus on it)

Target Market(s)

Target group: Founder (20-50 yrs, m / w, needy, in "break-up phase") and CONTRACTOR / "financier" (30-55 yrs, m / w, often public service "routine-oriented"). The foundations are in quite different industries: digital, craft, tourism, retail, services, etc. Almost all German.

Industry/Entity Type

Consultant

Contact Information for Business Card

Lukas Brandvik
M. Sc., International Business Administration
Gründungsberater, Konzeptentwickler
www.falkenhorn-beratung.de
kontakt@falkenhorn-beratung.de
Tel. 0471 239 5518

Colors

Designer to choose colors to be used in the design.

Requirements
Must have
• Professionalism, persuasiveness, clarity
Nice to have
• memorability
Should not have
• Schnörkelei

```html
<!DOCTYPE html>
<html lang="de">
<head>
<meta charset="utf-8">
<title>Lukas Brandvik – Visitenkarte</title>
<link href="https://fonts.googleapis.com/css2?family=Dosis:wght@300;400;700&display=swap" rel="stylesheet">
<style>
  :root {
    --bg: #cbcbcb;
    --ink: #231f20;
    --paper: #ffffff;
    --green: #8dc63f;
    --text-dark: #231f20;
  }
  * { margin: 0; padding: 0; box-sizing: border-box; }
  html, body { width: 1200px; height: 1200px; overflow: hidden; background: var(--bg); font-family: "Dosis", sans-serif; }
  .card { position: absolute; width: 604px; height: 403px; overflow: hidden; }
  .card::after { content: ""; position: absolute; top: 0; right: 0; width: 34px; height: 100%; background: var(--green); }
  .card--front { left: 126px; top: 151px; background: var(--ink); color: var(--paper); }
  .card--back { left: 448px; top: 589px; background: var(--paper); color: var(--text-dark); }

  .brand { position: absolute; left: 186px; top: 126px; width: 200px; display: flex; align-items: center; justify-content: center; gap: 10px; }
  .brand__square { width: 22px; height: 22px; background: var(--green); }
  .brand__name { font-weight: 400; font-size: 26px; letter-spacing: 1px; color: var(--paper); line-height: 1; }

  .name { font-weight: 700; font-size: 60px; line-height: 1; letter-spacing: -0.5px; white-space: nowrap; }
  .degree { font-weight: 300; font-size: 21px; line-height: 1; white-space: nowrap; }

  .card--front .name { position: absolute; left: 0; width: 572px; text-align: center; top: 236px; }
  .card--front .degree { position: absolute; left: 0; width: 572px; text-align: center; top: 292px; }

  .card--back .name { position: absolute; right: 54px; top: 64px; }
  .card--back .degree { position: absolute; right: 54px; top: 120px; }

  .roles { position: absolute; left: 66px; top: 170px; color: var(--green); font-weight: 400; font-size: 22px; line-height: 28px; }
  .contact { position: absolute; left: 36px; display: flex; align-items: center; gap: 10px; font-size: 23px; font-weight: 400; line-height: 1; }
  .contact svg { width: 20px; height: 20px; fill: var(--green); flex: none; }
  .contact--phone { top: 248px; }
  .contact--mail { top: 297px; }
  .contact--web { top: 346px; }
</style>
</head>
<body>
  <section class="card card--front">
    <div class="brand">
      <span class="brand__square"></span>
      <span class="brand__name">Falkenhorn</span>
    </div>
    <div class="name">Lukas Brandvik</div>
    <div class="degree">M. SC., INTERNATIONAL BUSINESS ADMINISTRATION</div>
  </section>

  <section class="card card--back">
    <div class="name">Lukas Brandvik</div>
    <div class="degree">M. SC., INTERNATIONAL BUSINESS ADMINISTRATION</div>
    <div class="roles">Gründungsberater<br>Konzeptentwickler</div>

    <div class="contact contact--phone">
      <svg viewBox="0 0 20 20" aria-hidden="true"><path d="M4 1.5l3 .5 1.2 4-2 1.6c1 2.3 2.8 4.1 5 5.1l1.7-2 4 1.2.6 3-2.2 2.3C9 17 3 11 1.8 3.8z"/></svg>
      <span>0471 239 5518</span>
    </div>
    <div class="contact contact--mail">
      <svg viewBox="0 0 20 20" aria-hidden="true"><path d="M0 4h20v12H0z M1.5 5.2L10 11l8.5-5.8" /><path d="M1.3 5l8.7 6 8.7-6" fill="none" stroke="#fff" stroke-width="1.3"/><path d="M0.8 15.2l6.5-5.4M19.2 15.2l-6.5-5.4" stroke="#fff" stroke-width="1.1"/></svg>
      <span>kontakt@falkenhorn-beratung.de</span>
    </div>
    <div class="contact contact--web">
      <svg viewBox="0 0 20 20" aria-hidden="true"><circle cx="10" cy="10" r="9.5"/><path d="M10 2a8 8 0 0 0-6.7 3.7c1.5.5 2.3 1.8 3.8 1.6 1.4-.2 1-2 2.6-2.6 1-.4 1.3-1.4.9-2.4zM12.5 9c-1.6.3-2.3 2-1.6 3.5.5 1.2.2 2.5 1 3.8 2.2-.9 4-3 4.4-5.4-1.2-.4-2.4-2.2-3.8-1.9z" fill="#fff"/></svg>
      <span>www.falkenhorn-beratung.de</span>
    </div>
  </section>
</body>
</html>
```